Vela Brook Services Site Redesign

SIte redesign for a commercial/residential cleaning and restoration company.

Design style should be as for a professional service company. Use this as a guide: https://nimbora.quellworks.example/electrician/

Please use current site content located here: http://vbsgrn.example/

Design should be responsive

Site Design should include two (2) pages:
- Homepage
- Interior page (for services) with a layout that can be duplicated across the different interior pages

Please Use the following items for the Navigation:
• Water Damage Restoration
• Fire & Smoke Damage Restoration
• Remodeling
• Roofing
• New Flooring Sales and Installation
• 24HR Emergency Services
• Commercial Services

Add BOLD, red Call To Action of "CALL NOW" on homepage

Feature image to be around water damage restoration and emergency services (flooded home) – similar to this photo: http://vbsgrn.example/images/flood.jpg

Add work and projects section

Keep services icons and descriptions with main focus is Water damage, Fire damage, Storm damage, Roof repair replacement, Exterior repairs and Kitchen/Bath Remodeling

Target Market(s)

Customers looking for home disaster restoration services

Number of Pages Required

2 page

Requirements
Must have
• Responsive Design
• 2 pages submitted - Homepage & Interior page. Designs WILL NOT be considered if 2 pages aren't submitted

```html
<!DOCTYPE html>
<html lang="en">
<head>
<meta charset="utf-8">
<title>Vela Brook Services – Homepage and Service Page</title>
<link href="https://fonts.googleapis.com/css2?family=Lato:wght@400;700;900&display=swap" rel="stylesheet">
<style>
:root{
  --blue:#0a0a8c;
  --blue-dark:#07076e;
  --red:#c8161d;
  --ink:#333;
  --muted:#666;
  --panel:#f0f0f0;
  --canvas:#b3b3b3;
  --white:#fff;
}
*{box-sizing:border-box;margin:0;padding:0}
html,body{width:800px;height:1200px;overflow:hidden;background:var(--canvas);font-family:"Lato",Arial,sans-serif;color:var(--ink)}
.board{position:absolute;left:0;top:0;width:1000px;height:1500px;transform:scale(.8);transform-origin:0 0}
.page{position:absolute;background:var(--white);overflow:hidden}
.page--home{left:22px;top:22px;width:468px;height:1421px}
.page--service{left:509px;top:22px;width:469px;height:856px}
.abs{position:absolute}

/* header */
.site-header{position:absolute;left:0;top:0;width:100%;height:37px;background:var(--white)}
.brand{position:absolute;left:53px;top:11px;display:flex;align-items:center;gap:4px;color:var(--blue);font-weight:900;font-size:10px;letter-spacing:.2px;white-space:nowrap}
.brand-mark{width:9px;height:9px;background:var(--blue)}
.hours{position:absolute;left:256px;top:10px;font-size:5px;color:var(--muted)}
.phones{position:absolute;left:222px;top:17px;font-size:9.5px;font-weight:700;color:var(--blue);white-space:nowrap}
.call-now{position:absolute;left:367px;top:10px;width:50px;height:20px;background:var(--red);color:var(--white);font-weight:900;font-size:8px;display:flex;align-items:center;justify-content:center;letter-spacing:.2px}
.main-nav{position:absolute;left:0;top:37px;width:100%;height:14px;background:var(--blue);color:var(--white);font-size:3.6px;display:flex;align-items:center;justify-content:center;white-space:nowrap}
.main-nav span+span:before{content:"|";margin:0 3px}

/* hero */
.hero{position:absolute;left:0;top:51px;width:100%;height:189px;background:linear-gradient(180deg,#8c8c86 0%,#a7a49b 35%,#6f7670 65%,#4f5c58 100%)}
.hero-cap{position:absolute;left:172px;top:205px;width:122px;height:18px;background:rgba(0,0,0,.45);color:var(--white);font-size:8px;letter-spacing:.4px;display:flex;align-items:center;justify-content:center}
.hero-arrow{position:absolute;top:141px;width:9px;height:9px;background:#111;color:#fff;font-size:6px;display:flex;align-items:center;justify-content:center}

/* generic section */
.band{position:absolute;left:0;width:100%}
.band--gray{background:var(--panel)}
.section-title{position:absolute;left:0;width:100%;text-align:center;color:var(--blue);font-weight:700;font-size:9px}
.lead{position:absolute;text-align:center;font-size:5.3px;line-height:1.72;color:var(--muted)}
.lead b{color:var(--blue);font-weight:400}

/* service tiles */
.tile{position:absolute;background:var(--blue);color:var(--white);display:flex;flex-direction:column;align-items:center;justify-content:flex-end;font-size:5.6px;padding-bottom:9px;text-align:center}
.tile svg{width:26px;height:24px;margin-bottom:5px;fill:none;stroke:#fff;stroke-width:1.1}
.tile--side{font-size:5.4px;padding-bottom:8px}

/* feature cards */
.photo{position:absolute}
.feature-title{position:absolute;font-size:7.5px;color:var(--blue)}
.feature-text{position:absolute;font-size:3.5px;line-height:1.6;color:var(--muted);width:116px}
.btn{position:absolute;height:15px;background:var(--blue);color:var(--white);font-size:4.6px;display:flex;align-items:center;justify-content:center}

/* testimonials */
.quote{position:absolute;width:115px;height:111px;background:var(--white);border:1px solid #d8d8d8;text-align:center}
.avatar{position:absolute;left:40px;top:11px;width:34px;height:34px;border-radius:50%;background:radial-gradient(circle at 50% 40%,#c9b39d 0%,#8a7866 60%,#d9d9d9 62%)}
.quote p{position:absolute;left:12px;right:12px;top:52px;font-size:4px;line-height:1.7;color:var(--muted)}
.quote .who{position:absolute;left:0;width:100%;top:88px;font-size:5px;color:#222}
.quote .role{position:absolute;left:0;width:100%;top:95px;font-size:3.6px;color:var(--muted)}
.chev{position:absolute;font-size:12px;color:#888;line-height:1}

/* badges */
.badge{position:absolute;width:113px;height:50px;background:#eee}
.badge-seal{position:absolute;left:7px;top:9px;width:32px;height:32px;background:var(--white)}
.badge-seal i{position:absolute;left:8px;top:8px;width:16px;height:16px}
.badge-text{position:absolute;left:48px;top:10px;width:60px;font-size:5.2px;line-height:1.6;color:var(--muted)}
.badge-text small{display:block;font-size:3px;line-height:1.5;margin-top:2px}

/* footer */
.site-footer{position:absolute;left:0;width:100%;background:var(--blue);color:#cfd0f0}
.foot-nav{position:absolute;left:0;width:100%;text-align:center;font-size:3.6px;white-space:nowrap}
.foot-nav span+span:before{content:"|";margin:0 2.5px}
.copy{position:absolute;left:0;width:100%;text-align:center;font-size:3.8px}
.pay{position:absolute;display:flex;gap:4px}
.pay i{width:9px;height:6px;background:#aeb0e0;display:block}
.social{position:absolute;display:flex;gap:5px}
.social i{width:5px;height:5px;border-radius:50%;background:#aeb0e0;display:block}

/* service page article */
.article-head{position:absolute;left:52px;top:82px;display:flex;align-items:center;gap:9px;color:var(--blue);font-size:9px;font-weight:700}
.article-head svg{width:25px;height:25px;fill:none;stroke:var(--blue);stroke-width:1.1}
.article{position:absolute;left:52px;top:115px;width:272px;font-size:4.5px;line-height:1.75;color:#444}
.article p{margin-bottom:6px}
</style>
</head>
<body>
<svg width="0" height="0" style="position:absolute">
  <defs>
    <symbol id="i-water" viewBox="0 0 26 24"><path d="M4 12 13 4l9 8M7 10v7h12v-7M11 17v-4h4v4"/><path d="M1 20c2-2 4 2 6 0s4 2 6 0 4 2 6 0 4 2 6 0M1 23c2-2 4 2 6 0s4 2 6 0 4 2 6 0 4 2 6 0"/></symbol>
    <symbol id="i-fire" viewBox="0 0 26 24"><path d="M4 12 13 4l9 8M6 10v12h14V10M10 22v-5h6v5"/><path d="M13 2c-2 2-1 3 0 4 1-1 2-2 0-4zM9 5c-1 1 0 2 1 2M17 5c1 1 0 2-1 2"/><rect x="8" y="12" width="3" height="3"/><rect x="15" y="12" width="3" height="3"/></symbol>
    <symbol id="i-storm" viewBox="0 0 26 24"><path d="M7 14a4 4 0 0 1 0-8 6 6 0 0 1 11-1 4 4 0 0 1 1 9z"/><path d="M13 14l-2 4h3l-2 5M7 17l-1 3M19 17l-1 3M16 17l-1 2"/></symbol>
    <symbol id="i-roof" viewBox="0 0 26 24"><path d="M3 20 6 4h14l3 16zM5 12h16M4 16h18M9 4l-1 16M13 4v16M17 4l1 16"/></symbol>
    <symbol id="i-ext" viewBox="0 0 26 24"><path d="M2 11 13 3l11 8M5 9v13h16V9M11 22v-6h4v6"/><rect x="7" y="12" width="3" height="3"/><rect x="16" y="12" width="3" height="3"/><path d="M9 7h8"/></symbol>
    <symbol id="i-kitchen" viewBox="0 0 26 24"><rect x="2" y="3" width="9" height="6"/><rect x="15" y="3" width="9" height="6"/><rect x="2" y="13" width="22" height="9"/><path d="M13 13v9M5 16h5M16 16h5M6 11h2M18 11h2"/></symbol>
  </defs>
</svg>

<div class="board">

  <!-- HOMEPAGE -->
  <section class="page page--home">
    <header class="site-header">
      <div class="brand"><span class="brand-mark"></span>Vela Brook Services</div>
      <div class="hours">Flood Service 24 Hours / 7 Days a Week</div>
      <div class="phones">555-014-2207 &nbsp;| &nbsp;555-019-3861</div>
      <div class="call-now">Call Now</div>
    </header>
    <nav class="main-nav"><span>Water Damage Restoration</span><span>Fire &amp; Smoke Damage Restoration</span><span>Remodeling</span><span>Roofing</span><span>New Flooring Sales and Installation</span><span>24HR Emergency Services</span><span>Commercial Services</span></nav>

    <div class="hero" role="img" aria-label="Flooded living room with furniture standing in water"></div>
    <div class="hero-arrow" style="left:0">&#8249;</div>
    <div class="hero-arrow" style="left:459px">&#8250;</div>
    <div class="hero-cap">DALLAS - FORT WORTH</div>

    <div class="section-title" style="top:269px">Welcome to Vela Brook Services</div>
    <p class="lead" style="left:54px;width:360px;top:284px">Vela Brook Services is more than just a carpet cleaning company. Our customers also count on us for tile and grout cleaning, upholstery cleaning, carpet repair, stain removal, flood and fire damage restoration. Always on call, we are ready to spring into action 24 hours a day if you need emergency service. Moreover, we provide full service carpet and tile sales and installation.</p>

    <div class="band band--gray" style="top:348px;height:245px"></div>
    <div class="section-title" style="top:377px">Services</div>
    <p class="lead" style="left:54px;width:360px;top:392px;font-size:4.4px">Vela Brook Services provides service to all of the Dallas/Fort Worth metroplex area including <b>Dallas, Plano, Garland, Frisco, Rockwall, Rowlett, Carrollton, Coppell, Addison, Highland Park, University Park, Grand Prairie, and more.</b> Call or Email us today to find out if you are in our service area.</p>

    <div class="tile" style="left:52px;top:421px;width:115px;height:60px"><svg><use href="#i-water"/></svg>Water damage</div>
    <div class="tile" style="left:177px;top:421px;width:115px;height:60px"><svg><use href="#i-fire"/></svg>Fire damage</div>
    <div class="tile" style="left:302px;top:421px;width:115px;height:60px"><svg><use href="#i-storm"/></svg>Storm damage</div>
    <div class="tile" style="left:52px;top:493px;width:115px;height:60px"><svg><use href="#i-roof"/></svg>Roof repair replacement</div>
    <div class="tile" style="left:177px;top:493px;width:115px;height:60px"><svg><use href="#i-ext"/></svg>Exterior repairs</div>
    <div class="tile" style="left:302px;top:493px;width:115px;height:60px"><svg><use href="#i-kitchen"/></svg>Kitchen/Bath Remodeling</div>

    <div class="photo" style="left:52px;top:625px;width:113px;height:73px;background:linear-gradient(160deg,#9aa3a3,#5f6b6c)" role="img" aria-label="Flooded office building interior"></div>
    <div class="photo" style="left:178px;top:625px;width:113px;height:73px;background:linear-gradient(160deg,#8d8a80,#4c4a44 60%,#d3b53a)" role="img" aria-label="Mopped commercial floor with a yellow wet floor sign"></div>
    <div class="photo" style="left:304px;top:625px;width:113px;height:73px;background:linear-gradient(160deg,#d8d2c6,#b9b0a2)" role="img" aria-label="Carpet being cleaned with an extraction wand"></div>
    <div class="feature-title" style="left:52px;top:702px">Emergency Service</div>
    <div class="feature-title" style="left:178px;top:702px">Commercial Services</div>
    <div class="feature-title" style="left:304px;top:702px">Get Pricing</div>
    <div class="feature-text" style="left:52px;top:716px">Fires and floods rarely wait and it is convenient. This is why we are available 24 hours a day to handle your emergency.</div>
    <div class="feature-text" style="left:178px;top:716px">We have special rates and services for commercial clients.</div>
    <div class="feature-text" style="left:304px;top:716px">Request pricing and apply for your online discount code.</div>
    <div class="btn" style="left:52px;top:732px;width:43px">Contact Us</div>
    <div class="btn" style="left:178px;top:732px;width:43px">Get a Quote</div>
    <div class="btn" style="left:304px;top:732px;width:43px">Get Pricing</div>

    <div class="band band--gray" style="top:780px;height:193px"></div>
    <div class="section-title" style="top:809px">Testimonials</div>
    <div class="chev" style="left:21px;top:880px">&#8249;</div>
    <div class="chev" style="left:440px;top:880px">&#8250;</div>
    <div class="quote" style="left:52px;top:830px"><div class="avatar" role="img" aria-label="Customer portrait"></div><p>Mauris suscipit felis id nunc elementum varius. Praesent elementum nulla sit amet justo pellentesque scelerisque. Nam et tortor in ante iaculis porttitor in luctus mi.</p><div class="who">- Aaron Lisle</div><div class="role">Vivamus gravida</div></div>
    <div class="quote" style="left:177px;top:830px"><div class="avatar" role="img" aria-label="Customer portrait" style="background:radial-gradient(circle at 50% 40%,#e2c9a0 0%,#c9a56b 60%,#d9d9d9 62%)"></div><p>Mauris suscipit felis id nunc elementum varius. Praesent elementum nulla sit amet justo pellentesque scelerisque. Nam et tortor in ante iaculis porttitor in luctus mi.</p><div class="who">- Mirela</div><div class="role">Vivamus gravida</div></div>
    <div class="quote" style="left:302px;top:830px"><div class="avatar" role="img" aria-label="Customer portrait" style="background:radial-gradient(circle at 50% 40%,#8a6e58 0%,#4a3a2f 60%,#d9d9d9 62%)"></div><p>Mauris suscipit felis id nunc elementum varius. Praesent elementum nulla sit amet justo pellentesque scelerisque. Nam et tortor in ante iaculis porttitor in luctus mi.</p><div class="who">- Dorian</div><div class="role">Vivamus gravida</div></div>

    <div class="section-title" style="top:1003px">Work and Projects</div>
    <div class="chev" style="left:22px;top:1109px;color:#222">&#8249;</div>
    <div class="chev" style="left:440px;top:1109px;color:#222">&#8250;</div>
    <div class="photo" style="left:52px;top:1022px;width:87px;height:91px;background:linear-gradient(150deg,#7b5a3c,#c4763a 50%,#3d3a36)" role="img" aria-label="Worker removing water damaged drywall"></div>
    <div class="photo" style="left:144px;top:1022px;width:87px;height:91px;background:linear-gradient(150deg,#b99f74,#8a7252)" role="img" aria-label="Weathered wooden shutters on a wall"></div>
    <div class="photo" style="left:237px;top:1022px;width:180px;height:91px;background:linear-gradient(180deg,#2f5fa8,#6b8dc4 55%,#2c2e36)" role="img" aria-label="Crew in protective suits on a burned roof"></div>
    <div class="photo" style="left:52px;top:1119px;width:179px;height:85px;background:linear-gradient(150deg,#e4e4e2,#bdbdbb 60%,#2a2a2a)" role="img" aria-label="Air mover drying a floor"></div>
    <div class="photo" style="left:237px;top:1119px;width:87px;height:85px;background:linear-gradient(160deg,#f2f2f0,#cfcfcb)" role="img" aria-label="Renovated white kitchen cabinets"></div>
    <div class="photo" style="left:330px;top:1119px;width:87px;height:85px;background:linear-gradient(180deg,#d5d8dc,#6e7379 50%,#4a4e54)" role="img" aria-label="Slate roof with chimney"></div>

    <div class="band" style="top:1235px;height:1px;background:#e6e6e6"></div>
    <div class="badge" style="left:52px;top:1261px"><div class="badge-seal"><i style="background:#2f8a4a"></i></div><div class="badge-text">Certified by the Guild of Cleaning and Restoration Inspectors</div></div>
    <div class="badge" style="left:178px;top:1261px"><div class="badge-seal"><i style="background:var(--blue-dark)"></i></div><div class="badge-text">Fair Trade Business Council<small>We are proud members of the council and maintain an A+ rating</small></div></div>
    <div class="badge" style="left:304px;top:1261px"><div class="badge-seal"><i style="background:#2236b8"></i></div><div class="badge-text">Proud Member of the Clean Air Trade Association</div></div>

    <footer class="site-footer" style="top:1343px;height:78px">
      <div class="foot-nav" style="top:15px"><span>Water Damage Restoration</span><span>Fire &amp; Smoke Damage Restoration</span><span>Remodeling</span><span>Roofing</span><span>New Flooring Sales and Installation</span><span>24HR Emergency Services</span><span>Commercial Services</span></div>
      <div class="copy" style="top:26px">Copyright © 2018 Vela Brook Services. All rights reserved.</div>
      <div class="pay" style="left:52px;top:55px"><i></i><i></i><i></i><i></i><i></i></div>
      <div class="social" style="left:359px;top:56px"><i></i><i></i><i></i><i></i><i></i></div>
    </footer>
  </section>

  <!-- SERVICE PAGE -->
  <section class="page page--service">
    <header class="site-header">
      <div class="brand"><span class="brand-mark"></span>Vela Brook Services</div>
      <div class="hours">Flood Service 24 Hours / 7 Days a Week</div>
      <div class="phones">555-014-2207 &nbsp;| &nbsp;555-019-3861</div>
      <div class="call-now">Call Now</div>
    </header>
    <nav class="main-nav"><span>Water Damage Restoration</span><span>Fire &amp; Smoke Damage Restoration</span><span>Remodeling</span><span>Roofing</span><span>New Flooring Sales and Installation</span><span>24HR Emergency Services</span><span>Commercial Services</span></nav>

    <div class="article-head"><svg><use href="#i-water"/></svg>Water damage</div>
    <div class="article">
      <p>Do you have time for flooding and the damage it causes to interrupt your life?</p>
      <p>We at Vela Brook know you don't have that kind of time. Call us 24 hours a day for emergencies that disrupt your life.</p>
      <p>Our technicians are here when you need them for a quick, effective response. Vela Brook can remove the excess water and expedite the process of drying your home. Our professional specialists use our standard process from structural repair and content restoration to deodorizing rooms and doing the final clean up to get you home back to normal.</p>
      <p>Vela Brook is ready 24 hours a day, 7 days a week to take your calls and minimize disruptions and disturbances in your life. We will also work closely with your insurance company to help you get your life back in order in the shortest amount of time possible.</p>
    </div>
    <div class="photo" style="left:53px;top:236px;width:271px;height:203px;background:linear-gradient(180deg,#dcdad6 0%,#c9c6c0 45%,#8d8170 70%,#6d614f 100%)" role="img" aria-label="Living room flooded with brown water around a grey sofa"></div>

    <div class="tile tile--side" style="left:334px;top:83px;width:83px;height:69px"><svg><use href="#i-fire"/></svg>Fire damage</div>
    <div class="tile tile--side" style="left:334px;top:155px;width:83px;height:69px"><svg><use href="#i-storm"/></svg>Storm damage</div>
    <div class="tile tile--side" style="left:334px;top:227px;width:83px;height:69px"><svg><use href="#i-roof"/></svg>Roof repair replacement</div>
    <div class="tile tile--side" style="left:334px;top:299px;width:83px;height:69px"><svg><use href="#i-ext"/></svg>Exterior repairs</div>
    <div class="tile tile--side" style="left:334px;top:371px;width:83px;height:69px"><svg><use href="#i-kitchen"/></svg>Kitchen/Bath Remodeling</div>

    <div class="band band--gray" style="top:472px;height:193px"></div>
    <div class="section-title" style="top:501px">Testimonials</div>
    <div class="chev" style="left:21px;top:571px">&#8249;</div>
    <div class="chev" style="left:440px;top:571px">&#8250;</div>
    <div class="quote" style="left:52px;top:522px"><div class="avatar" role="img" aria-label="Customer portrait"></div><p>Mauris suscipit felis id nunc elementum varius. Praesent elementum nulla sit amet justo pellentesque scelerisque. Nam et tortor in ante iaculis porttitor in luctus mi.</p><div class="who">- Aaron Lisle</div><div class="role">Vivamus gravida</div></div>
    <div class="quote" style="left:177px;top:522px"><div class="avatar" role="img" aria-label="Customer portrait" style="background:radial-gradient(circle at 50% 40%,#e2c9a0 0%,#c9a56b 60%,#d9d9d9 62%)"></div><p>Mauris suscipit felis id nunc elementum varius. Praesent elementum nulla sit amet justo pellentesque scelerisque. Nam et tortor in ante iaculis porttitor in luctus mi.</p><div class="who">- Mirela</div><div class="role">Vivamus gravida</div></div>
    <div class="quote" style="left:302px;top:522px"><div class="avatar" role="img" aria-label="Customer portrait" style="background:radial-gradient(circle at 50% 40%,#8a6e58 0%,#4a3a2f 60%,#d9d9d9 62%)"></div><p>Mauris suscipit felis id nunc elementum varius. Praesent elementum nulla sit amet justo pellentesque scelerisque. Nam et tortor in ante iaculis porttitor in luctus mi.</p><div class="who">- Dorian</div><div class="role">Vivamus gravida</div></div>

    <div class="badge" style="left:52px;top:697px"><div class="badge-seal"><i style="background:#2f8a4a"></i></div><div class="badge-text">Certified by the Guild of Cleaning and Restoration Inspectors</div></div>
    <div class="badge" style="left:178px;top:697px"><div class="badge-seal"><i style="background:var(--blue-dark)"></i></div><div class="badge-text">Fair Trade Business Council<small>We are proud members of the council and maintain an A+ rating</small></div></div>
    <div class="badge" style="left:304px;top:697px"><div class="badge-seal"><i style="background:#2236b8"></i></div><div class="badge-text">Proud Member of the Clean Air Trade Association</div></div>

    <footer class="site-footer" style="top:779px;height:77px">
      <div class="foot-nav" style="top:15px"><span>Water Damage Restoration</span><span>Fire &amp; Smoke Damage Restoration</span><span>Remodeling</span><span>Roofing</span><span>New Flooring Sales and Installation</span><span>24HR Emergency Services</span><span>Commercial Services</span></div>
      <div class="copy" style="top:26px">Copyright © 2018 Vela Brook Services. All rights reserved.</div>
      <div class="pay" style="left:52px;top:56px"><i></i><i></i><i></i><i></i><i></i></div>
      <div class="social" style="left:359px;top:57px"><i></i><i></i><i></i><i></i><i></i></div>
    </footer>
  </section>

</div>
</body>
</html>
```